Etiketten-Design für Honiggläser
Die Zusammenarbeit mit Mirko war sehr unkompliziert. Änderungswünsche wurden prompt umgesetzt und die Beratung war hervorragend! Besten Dank für das tolle Etikett!
Zielgruppe
Wir sind Imker und benötigen Etiketten für Honiggläser.
Aufgabenstellung
Siehe Anlage. Es sollen keine Fotos verwendet werden. Grafiken sind in Ordnung.
Etiketten-Design für Honigglas Etiketten-Design für Honigglas"
Format: Etikett für 250-gr.-Honigglas (TO ∅ 63 mm). Standardmaßgrösse 165 × 40 mm Design: schlicht, hochwertig, modern, edel/royal, unkonventionelles Design (weg von Bienen, Waben, Landschaften usw.), dunkle Farbtöne in Kontrast zu heller Schrift, die beiden Textbausteine 'Los Nr. ' sowi..
Attraktives Etiketten-Design für Honig Attraktives Etiketten-Design für Honig"
Wir verkaufen zur Zeit vor allem Waldhonig, streben aber auch einen Blütenhonig an. Das Etikett soll daher entweder den Wald wiederspiegeln oder aber neutral sein, so dass der Schriftzug Waldhonig oder Blütenhonig jeweils eingesetzt werden kann. Wichtig ist mir der Ortszusatz 'aus dem Glottertal..
Etiketten-Design für Produkte eines Familienbetriebs mit Imkerei und Hühnerhaltung Etiketten-Design für Produkte eines Familienbetriebs mit Imkerei und Hühnerhaltung"
1. Zentrale, auf allen Etiketten wiederkehrende Elemente: - Unser Riegelhaus (stilisiert) (Bild beiliegend) - Das Wort 'Feldrain' (Anmerkung: ohne Anführungszeichen) - die zentralen Elemente sollen die Produkte nicht überragen. 2. Dezente Adresse: - Familie Ruppelt, Kiesgrund, CH-9612 Tobelried 3...
Etiketten-Design für Kurkuma-Honig Etiketten-Design für Kurkuma-Honig"
Etikett für 500g // Stanze eckig (210x35mm), Druckdatei entsprechend Vorgaben https://etikora-druck.de/faq/ Vorgaben für das Grünspan Logo im Anhang Vorgaben für EG Öko Logo : https://oeko-siegelamt.example/downloads/logo_de Pflichtangaben auf dem Etikett: Gewicht, Adresse siehe Beispiel..
Etiketten-Design für Blütenhonig und Waldhonig gesucht Etiketten-Design für Blütenhonig und Waldhonig gesucht"
Zwei verschiedene Etiketten-Desings 1 x Blütenhonig sowie 1 x Waldhonig für unterschiedliche Honigglasgrößen (500 g und 250 g) Die Maße für die Etiketten wären: Für 500-Gramm-Glas 210 mm x 45 mm für's 250-Gramm-Glas 180 mm x 38 mm. Wir sind auch offen für neue Vorschläge bezüglich ..

```html
<!DOCTYPE html>
<html lang="de">
<head>
<meta charset="utf-8">
<title>Honigglas-Etikett Frühtracht</title>
<link rel="stylesheet" href="https://fonts.googleapis.com/css2?family=Great+Vibes&family=Roboto+Condensed:wght@400&display=swap">
<style>
  :root {
    --canvas: #ffffff;
    --label: #dcd8d1;
    --ink: #4b1c1b;
    --text-grey: #3d3a37;
    --gold-light: #fbe58a;
    --gold: #e9b93a;
    --gold-deep: #c77d1c;
    --bee-dark: #2a2520;
    --bee-wing: #ebe9e4;
  }
  * { box-sizing: border-box; margin: 0; padding: 0; }
  html, body { width: 1200px; height: 1158px; overflow: hidden; background: var(--canvas); }
  .artboard { position: relative; width: 1200px; height: 1158px; }
  .shapes { position: absolute; inset: 0; }
  .script { font-family: "Great Vibes", cursive; color: var(--ink); position: absolute; line-height: 1; white-space: nowrap; }
  .neck-region { font-size: 46px; left: 578px; top: 104px; transform: rotate(-12deg); transform-origin: left bottom; }
  .neck-product { font-size: 84px; left: 480px; top: 172px; }
  .variety { position: absolute; left: 401px; width: 436px; top: 788px; text-align: center;
    font-family: "Roboto Condensed", sans-serif; font-size: 17px; color: #5a5550; letter-spacing: .3px; }
  .product-name { font-size: 76px; left: 360px; width: 436px; text-align: center; top: 828px; }
  .side-text { position: absolute; writing-mode: vertical-rl; transform: rotate(180deg);
    font-family: "Roboto Condensed", sans-serif; font-size: 12.5px; line-height: 20px;
    color: var(--text-grey); letter-spacing: .4px; white-space: nowrap; }
  .info-storage { left: 188px; bottom: 80px; height: 300px; }
  .info-producer { left: 900px; bottom: 80px; height: 340px; }
  .best-before-box { position: absolute; left: 987px; top: 750px; width: 38px; height: 78px;
    background: #f6f5f2; border: 1px solid #c9c5be; }
</style>
</head>
<body>
<div class="artboard">
  <svg class="shapes" width="1200" height="1158" viewBox="0 0 1200 1158">
    <defs>
      <linearGradient id="ring-gold" x1="0" y1="0" x2="1" y2="1">
        <stop offset="0" stop-color="var(--gold-light)"/>
        <stop offset=".45" stop-color="var(--gold-deep)"/>
        <stop offset=".7" stop-color="var(--gold)"/>
        <stop offset="1" stop-color="var(--gold-deep)"/>
      </linearGradient>
      <linearGradient id="panel-gold" x1="0" y1="0" x2="1" y2="1">
        <stop offset="0" stop-color="var(--gold)"/>
        <stop offset=".5" stop-color="var(--gold-light)"/>
        <stop offset="1" stop-color="var(--gold-deep)"/>
      </linearGradient>
      <linearGradient id="bee-tone" x1="0" y1="0" x2="1" y2="0">
        <stop offset="0" stop-color="var(--bee-wing)"/>
        <stop offset=".5" stop-color="var(--bee-dark)"/>
        <stop offset="1" stop-color="var(--bee-wing)"/>
      </linearGradient>
    </defs>

    <path class="neck-strip" d="M520 400 H679 V716 Q679 728 667 728 H532 Q520 728 520 716 Z" fill="var(--label)"/>
    <circle class="neck-ring" cx="599" cy="245" r="181" fill="url(#ring-gold)"/>
    <circle class="neck-face" cx="599" cy="245" r="165" fill="var(--label)"/>
    <ellipse class="neck-bee" role="img" aria-label="Illustration einer Biene mit Blüten" cx="575" cy="314" rx="119" ry="80" fill="url(#bee-tone)" opacity=".55"/>

    <rect class="body-label" x="155" y="728" width="884" height="370" fill="var(--label)"/>
    <rect class="gold-panel" role="img" aria-label="Goldenes Jugendstil-Ornament" x="376" y="728" width="436" height="370" fill="url(#panel-gold)"/>
    <ellipse class="panel-window" cx="594" cy="915" rx="196" ry="160" fill="var(--label)"/>
    <ellipse class="body-bee" role="img" aria-label="Illustration einer Biene mit Blüten" cx="658" cy="986" rx="132" ry="82" fill="url(#bee-tone)" opacity=".55"/>
  </svg>

  <div class="script neck-region">Bayern</div>
  <div class="script neck-product">Honig</div>

  <div class="variety">Blütenhonig cremig</div>
  <div class="script product-name">Frühtracht</div>

  <div class="side-text info-storage">
    Bienenhonig kristallisiert bei längerer Lagerung. Durch<br>
    Erwärmen im Wasserbad bei 40° C kann Honig ohne<br>
    Schaden wieder verflüssigt werden.<br>
    Ursprungsland: Deutschland, Bayern
  </div>

  <div class="side-text info-producer">
    Imkerei Brennwald Lindenweg 12, 85999 Mooshausen<br>
    info@imkerei-brennwald.de<br>
    Kühl, dunkel und trocken lagern.<br>
    Mehrwegglas - Bitte zurück zum Imker<br>
    <br>
    Blütenhonig 500g&nbsp;&nbsp;&nbsp;&nbsp;&nbsp;Haltbar bis:
  </div>
  <div class="best-before-box"></div>
</div>
</body>
</html>
```